Security camera surveillance warning Sign

Security Camera Sign 11" x 11" Red, Yellow and Black (White Background)
I would like a line drawing of camera image attached.
Wording: All Suspicious or Criminal Activity Will Be Reported!
WARNING
24 HOUR SURVEILLANCE

Industry/Entity Type

Security

Colors
ec1f27
000000
ffc214

Requirements
Nice to have
• I uploaded a sign and would like the new design look something like that

```html
<!DOCTYPE html>
<html lang="en">
<head>
<meta charset="utf-8">
<title>24 Hour Surveillance Warning Sign</title>
<link rel="stylesheet" href="https://fonts.googleapis.com/css2?family=Archivo+Black&family=Roboto+Condensed:wght@700;800&display=swap">
<style>
  :root {
    --sign-red: #ec1f27;
    --sign-yellow: #ffc214;
    --sign-black: #000000;
    --sign-white: #ffffff;
    --art-light: #ececec;
    --art-mid: #cfcfcf;
  }
  html, body {
    margin: 0;
    padding: 0;
    width: 1200px;
    height: 1200px;
    overflow: hidden;
    background: var(--sign-white);
  }
  .sign {
    position: relative;
    width: 1200px;
    height: 1200px;
    background: var(--sign-white);
  }
  .sign-frame {
    position: absolute;
    left: 22px; top: 22px;
    width: 1156px; height: 1156px;
    box-sizing: border-box;
    border: 8px solid var(--sign-black);
    border-radius: 48px;
    background: var(--sign-red);
  }
  .header-plate {
    position: absolute;
    left: 88px; top: 68px;
    width: 1026px; height: 182px;
    box-sizing: border-box;
    background: var(--sign-yellow);
    border: 9px solid var(--sign-black);
    border-radius: 14px;
    display: flex;
    align-items: center;
    justify-content: center;
  }
  .header-title {
    font-family: "Archivo Black", "Arial Black", sans-serif;
    font-size: 182px;
    line-height: 1;
    color: var(--sign-black);
    letter-spacing: 2px;
    transform: scaleX(1.02);
    margin-top: 6px;
  }
  .message-panel {
    position: absolute;
    left: 52px; top: 288px;
    width: 1096px; height: 724px;
    background: var(--sign-white);
  }
  .camera-art {
    position: absolute;
    left: 78px; top: 6px;
    width: 1000px; height: 470px;
    border-radius: 24px;
    background: linear-gradient(160deg, var(--art-light), var(--art-mid));
  }
  .notice {
    position: absolute;
    left: 24px; top: 492px;
    font-family: "Roboto Condensed", "Arial Narrow", sans-serif;
    font-weight: 800;
    color: var(--sign-black);
    text-transform: uppercase;
    line-height: 1.08;
  }
  .notice-line { display: block; }
  .notice-line--lead { font-size: 78px; letter-spacing: 0.5px; }
  .notice-line--middle { font-size: 57px; }
  .notice-line--close { font-size: 63px; }
  .footer-title {
    position: absolute;
    left: 0; top: 1012px;
    width: 1200px; height: 136px;
    display: flex;
    align-items: center;
    justify-content: center;
    font-family: "Roboto Condensed", "Arial Narrow", sans-serif;
    font-weight: 800;
    font-size: 90px;
    letter-spacing: 1px;
    color: var(--sign-white);
    text-transform: uppercase;
  }
</style>
</head>
<body>
  <main class="sign">
    <div class="sign-frame"></div>
    <div class="header-plate">
      <span class="header-title">WARNING</span>
    </div>
    <section class="message-panel">
      <div class="camera-art" role="img" aria-label="Line drawing of a wall-mounted security camera with sun hood on a bracket"></div>
      <p class="notice" style="margin:0;">
        <span class="notice-line notice-line--lead">All Suspicious</span>
        <span class="notice-line notice-line--middle">or Criminal Activity</span>
        <span class="notice-line notice-line--close">Will Be Recorded!</span>
      </p>
    </section>
    <div class="footer-title">24 Hour Surveillance</div>
  </main>
</body>
</html>
```